Residential Roofing Company, need a Unique business card for a Woman owned ompany

Woman Owned Residential Roofing Company. Specializing in Insurance Claims
Attention to Detail is what sets this woman owned roofing company apart from the rest
We are TRV Certified and are an Accredited business with an A rating with the QPL. Our Contractor License number KMT48395

```html
<!DOCTYPE html>
<html lang="en">
<head>
<meta charset="utf-8">
<title>Crestline Roofing – Business Card</title>
<link href="https://fonts.googleapis.com/css2?family=Montserrat:wght@400;500;600;800;900&display=swap" rel="stylesheet">
<style>
  :root {
    --navy: #0b2e66;
    --navy-tint: #c4d0e4;
    --navy-mist: #eef2f8;
    --ink: #111111;
    --grey-text: #5a5a5a;
    --paper: #ffffff;
    --backdrop: #a3a3a3;
    --badge-red: #d42a2f;
    --badge-blue: #12639a;
  }
  * { margin: 0; padding: 0; box-sizing: border-box; }
  html, body {
    width: 1200px; height: 1200px; overflow: hidden;
    background: var(--backdrop);
    font-family: "Montserrat", sans-serif;
  }
  .card-slot {
    position: absolute; left: 257px;
    width: 686px; height: 392px;
  }
  .card-slot.front { top: 165px; }
  .card-slot.back { top: 653px; }
  .card {
    position: absolute; top: 0; left: 0;
    width: 800px; height: 457px;
    background: var(--paper);
    transform: scale(0.8575); transform-origin: top left;
    overflow: hidden;
    box-shadow: 0 18px 30px rgba(0,0,0,0.25);
  }
  .card > * { position: absolute; }

  /* front */
  .brand {
    left: 64px; top: 92px;
    display: flex; align-items: center; gap: 16px;
    font-weight: 900; font-size: 36px; color: var(--ink);
    letter-spacing: -1px; line-height: 1;
  }
  .brand-mark { width: 46px; height: 46px; background: var(--navy); flex: none; }
  .address {
    left: 64px; top: 206px;
    font-size: 17px; line-height: 22px; color: var(--grey-text);
  }
  .address .license { margin-top: 4px; }
  .contact-list {
    left: 64px; top: 286px; list-style: none;
    font-size: 17px; line-height: 23px; color: var(--grey-text);
  }
  .contact-list li { display: flex; align-items: center; gap: 10px; }
  .contact-list svg { width: 15px; height: 15px; fill: var(--navy); }
  .person { right: 58px; top: 244px; text-align: right; }
  .person-name { font-size: 27px; font-weight: 600; color: var(--navy); letter-spacing: 0.5px; }
  .person-title { font-size: 17px; color: var(--ink); margin-top: 2px; }
  .wave { left: 0; top: 0; width: 800px; height: 457px; }
  .website {
    left: 65px; top: 420px;
    font-size: 17px; font-weight: 500; color: #fff; letter-spacing: 1px;
  }

  /* back */
  .roofline-art {
    left: 20px; top: 105px; width: 755px; height: 213px;
    background: linear-gradient(180deg, var(--navy-mist) 0%, var(--navy-tint) 100%);
  }
  .tag-band {
    left: 0; top: 323px; width: 800px; height: 35px;
    background: var(--navy); color: #fff;
    display: flex; align-items: center; justify-content: center; gap: 14px;
    font-size: 24px;
  }
  .tag-band strong { font-weight: 800; letter-spacing: 5px; }
  .tag-band span { font-weight: 400; letter-spacing: 4.5px; font-size: 21px; }
  .certified-badge {
    left: 48px; top: 380px; width: 148px; height: 56px;
    background: var(--badge-red);
  }
  .back-brand {
    left: 0; width: 800px; top: 388px; text-align: center;
    font-size: 34px; font-weight: 900; color: var(--ink); letter-spacing: -1px;
  }
  .accredited-badge {
    left: 640px; top: 378px; width: 122px; height: 58px;
    background: var(--badge-blue); border-radius: 6px;
  }
</style>
</head>
<body>

<section class="card-slot front">
  <div class="card">
    <div class="brand"><span class="brand-mark"></span>CRESTLINE ROOFING</div>

    <div class="address">
      <p>4218 Larkspur Way</p>
      <p>Anchorage, Alaska 34521</p>
      <p class="license">Lic No KMT48395</p>
    </div>

    <ul class="contact-list">
      <li><svg viewBox="0 0 24 24"><path d="M6.6 10.8a15.1 15.1 0 0 0 6.6 6.6l2.2-2.2c.3-.3.7-.4 1-.2 1.1.4 2.3.6 3.6.6.6 0 1 .4 1 1V20c0 .6-.4 1-1 1A17 17 0 0 1 3 4c0-.6.4-1 1-1h3.5c.6 0 1 .4 1 1 0 1.3.2 2.5.6 3.6.1.3 0 .7-.2 1z"/></svg>369-408-1732</li>
      <li><svg viewBox="0 0 24 24"><path d="M7 1h10a2 2 0 0 1 2 2v18a2 2 0 0 1-2 2H7a2 2 0 0 1-2-2V3a2 2 0 0 1 2-2zm0 3v14h10V4zm5 15.5a1 1 0 1 0 0 2 1 1 0 0 0 0-2z"/></svg>369-627-3190</li>
      <li><svg viewBox="0 0 24 24"><path d="M2 5h20v14H2zm2 2v.3l8 5.2 8-5.2V7zm0 2.7V17h16V9.7l-8 5.2z"/></svg>info@crestlineroofing.com</li>
    </ul>

    <div class="person">
      <p class="person-name">DANIEL REYES</p>
      <p class="person-title">President</p>
    </div>

    <svg class="wave" viewBox="0 0 800 457" aria-hidden="true">
      <path fill="var(--ink)" d="M0 424 C200 398 340 412 480 428 C620 444 740 450 800 404 L800 457 L0 457 Z"/>
      <path fill="var(--navy)" d="M0 416 C80 386 200 378 320 385 C480 394 620 414 700 410 C770 406 790 370 760 320 C805 360 808 408 782 424 C740 444 620 440 480 424 C340 408 200 394 0 420 Z"/>
    </svg>

    <p class="website">www.crestlineroofing.com</p>
  </div>
</section>

<section class="card-slot back">
  <div class="card">
    <div class="roofline-art" role="img" aria-label="Large roofline decoration of house gables with windows and a chimney"></div>
    <div class="tag-band"><strong>WOMAN OWNED</strong><span>ROOFING COMPANY</span></div>
    <div class="certified-badge" role="img" aria-label="TRV certified contractor badge"></div>
    <p class="back-brand">CRESTLINE ROOFING</p>
    <div class="accredited-badge" role="img" aria-label="QPL accredited business badge, rating A+"></div>
  </div>
</section>

</body>
</html>
```